Book cover

I need a cover for a my 3rd book that kinda goes with my brand (my previous book. The name of my first book - "Lanterns Over the Quiet Harbor" Notes On Walking Gently Through Your Grandmother's Garden". In the same style I need my third book - SLOW HARVEST" to stand out. I need a bolder, less whimsy cover, less playful. So can we use some of the same elements to stay consistent in this book cover. Perhaps use text to envoke emotions. This is the back cover so far (see below attachemnent)

Hello,
Subject: Cover Direction & Brand Consistency

Hi everyone,

Here’s my honest take: I don’t think the current execution fully reflects my brand yet. What I’m wondering is whether we can bring more continuity across my books—borrowing elements from my first and second covers to inform this third one. Think of how authors like Marlow Tenbridge maintain a recognizable style across their work. That consistency builds trust and signals authority before a reader even opens the book. Design choices like this matter more than we realize.

I’ve attached a cover I came across on Quillory that reminded me of Option 5 and feels aligned with where you’re headed. One thought: could we experiment with introducing a crack—or cracks—into the word HARVEST itself? Maybe put the title "SLOW HARVEST" at the edge of the cover vertically?

Curious to hear your thoughts and how you see this evolving.
P.s. Is there away to attach an idea?

SLOW HARVEST: Gathering Your Seasons in a Town that Forgets Stillness

```html
<!DOCTYPE html>
<html lang="en">
<head>
<meta charset="utf-8">
<title>Slow Harvest — Book Cover</title>
<link rel="stylesheet" href="https://fonts.googleapis.com/css2?family=Bebas+Neue&family=Oswald:wght@300&display=swap">
<style>
  :root {
    --page-bg: #ffffff;
    --sky-deep: #1c3a40;
    --sky-teal: #3e6468;
    --sky-mist: #9fb3a9;
    --horizon-glow: #f1e3c7;
    --horizon-warm: #e9c9a8;
    --ground-dusk: #4a5a5c;
    --ground-deep: #162629;
    --title-ink: #ffffff;
    --subtitle-ink: #0d0d0d;
    --author-ink: #ffffff;
  }
  html, body {
    margin: 0;
    width: 1200px;
    height: 1200px;
    overflow: hidden;
    background: var(--page-bg);
  }
  .cover {
    position: absolute;
    left: 237px;
    top: 54px;
    width: 734px;
    height: 1100px;
    overflow: hidden;
  }
  .cover-art {
    position: absolute;
    inset: 0;
    background: linear-gradient(
      to bottom,
      var(--sky-deep) 0%,
      var(--sky-teal) 22%,
      var(--sky-mist) 36%,
      var(--horizon-glow) 48%,
      var(--horizon-warm) 62%,
      var(--sky-mist) 70%,
      var(--ground-dusk) 78%,
      var(--ground-deep) 100%
    );
  }
  .title {
    position: absolute;
    left: 0;
    right: 0;
    margin: 0;
    text-align: center;
    font-family: "Bebas Neue", sans-serif;
    font-weight: 400;
    color: var(--title-ink);
    text-shadow: 0 2px 10px rgba(0, 0, 0, 0.25);
  }
  .title-line {
    display: block;
    position: absolute;
    left: 0;
    right: 0;
    line-height: 1;
    font-size: 226px;
  }
  .title-line--first { top: 33px; }
  .title-line--second { top: 211px; }
  .subtitle {
    position: absolute;
    left: 30px;
    right: 30px;
    top: 438px;
    margin: 0;
    text-align: center;
    font-family: "Bebas Neue", sans-serif;
    font-weight: 400;
    font-size: 51px;
    line-height: 50px;
    color: var(--subtitle-ink);
  }
  .author {
    position: absolute;
    left: 0;
    right: 0;
    top: 992px;
    margin: 0;
    text-align: center;
    font-family: "Oswald", sans-serif;
    font-weight: 300;
    font-size: 58px;
    letter-spacing: 0.12em;
    color: var(--author-ink);
  }
</style>
</head>
<body>
  <main class="cover">
    <div class="cover-art" role="img" aria-label="Photograph of a woman seen from behind standing on a runway facing a parked jet airliner under a stormy teal sky with a warm sunset glow on the horizon"></div>
    <h1 class="title">
      <span class="title-line title-line--first">SLOW</span>
      <span class="title-line title-line--second">HARVEST</span>
    </h1>
    <p class="subtitle">Gathering Your Seasons in a Town<br>That Forgets Stillness</p>
    <p class="author">CORALIE WINTERMERE</p>
  </main>
</body>
</html>
```